Business Card Needed for Crafter of Pottery, Jewelry and Artwork

Calling all designers in search of an artistic challenge.

I need a new business card design for my pottery, jewelry and artwork business, Woven Glass and Tide, based in Vancouver BC.

I would like a card that is bright and inviting and preferably incorporates my logo and a sample of photos of my work while having a clean fresh look. The following contact details would preferably be included on the card as well:
• Helena Pikeworth
• Designer
• Phone: 604.555.0172
• Email: Designer@WovenGlassandTide.example
• Website: www.WovenGlassandTide.example
• Blog: www.ShapingHillside.example

The logo is attached in two color schemes in both Vector and Source formats. On past cards I’ve also included photos of my work. By including photos of the work the pieces are showcased and it catches people’s eye and prompts them to pick up the card and look at it more closely. For example, if I leave a stack in a coffee shop I want people to be drawn to the card, to pick it up and get a sense of the my product lines. Please feel free to pull photos of my work directly off of my website. If you need photos with higher pixels please let me know and I’ll email them directly to you. The website background is bffbda (191, 251, 218). I would like the business cards to match the feel of the website for consistency but the cards do not need to use the exact same colors. My website and current business card are predominantly turquoise shades. The background uses stripes provided by the website template. I don’t know the exact colors of the stripes.

My current business card is attached to show the use of photos in a design. Please note that I am not thrilled with my own design and am looking for variations and completely new designs. This example is not meant to be used as a template or starting point.

Here is some background surrounding my company:
WGT offers one of a kind jewelry, pottery, artwork and leather bags each designed with a twist. The pottery varies from rustic every day functional ware to raku artwork. The jewelry ranges from simple sterling every day pieces to multimedia pieces incorporating stone, metal, ceramics and fabric. The artwork is multimedia, typically acrylic paired with a natural element such as bark. All the bags are leather with reworked kimono fabric or patterned silk lining.

Feel free to check out my website to get a flavour for my work and the color scheme I've used on marketing materials so far. www.wovenglassandtide.example
Updates

Thank you to everyone who has submitted a design so far. I hope everyone has received some helpful feedback.

I'm going to post a survey to customers and friends asking for their votes. If you have new designs to submit please try to get them in by Saturday March 30 at noon so that I can include it in the survey launch.

Thank you

Target Market(s)

Females aged 25-65 interested in one of a kind functional pottery and jewelry.

Industry/Entity Type

Coffee Shop

Requirements
Must have
• Contact information, website, blog
Nice to have
• Logo, photos

```html
<!DOCTYPE html>
<html lang="en">
<head>
<meta charset="utf-8">
<title>Woven Glass and Tide – Business Card</title>
<link rel="stylesheet" href="https://fonts.googleapis.com/css2?family=Caladea:wght@400;700&display=swap">
<style>
  :root {
    --stage: #464646;
    --ink: #0d1240;
    --teal: #1aa3ab;
    --teal-deep: #5cb3b3;
    --stripe-light: #a9dad8;
    --stripe-pale: #eef6f6;
    --stripe-mid: #8fcfcc;
    --ring: #9fd6d3;
    --white: #ffffff;
  }
  * { margin: 0; padding: 0; box-sizing: border-box; }
  html, body { width: 1200px; height: 846px; overflow: hidden; }
  body {
    background: var(--stage);
    position: relative;
    font-family: "Caladea", Georgia, serif;
    color: var(--ink);
  }
  .card {
    position: absolute;
    top: 171px;
    width: 292px;
    height: 509px;
    overflow: hidden;
  }
  .card--front {
    left: 251px;
    background: repeating-linear-gradient(to right,
      var(--stripe-light) 0 9px, var(--stripe-pale) 9px 14px,
      var(--stripe-light) 14px 17px, var(--stripe-pale) 17px 27px,
      var(--stripe-light) 27px 33px, var(--stripe-pale) 33px 38px);
  }
  .card--back {
    left: 635px;
    background: repeating-linear-gradient(to right,
      var(--teal-deep) 0 8px, var(--stripe-mid) 8px 14px,
      var(--teal-deep) 14px 18px, var(--stripe-mid) 18px 28px,
      var(--teal-deep) 28px 32px, var(--stripe-mid) 32px 38px);
  }
  .brand-seal {
    position: absolute;
    left: 48px;
    top: 37px;
    width: 194px;
    height: 194px;
    border-radius: 50%;
    background: var(--white);
    border: 2px solid var(--teal);
    display: flex;
    align-items: center;
    justify-content: center;
  }
  .brand-seal__disc {
    width: 178px;
    height: 178px;
    border-radius: 50%;
    background: var(--teal);
    display: flex;
    align-items: center;
    justify-content: center;
    text-align: center;
  }
  .brand-name {
    color: var(--white);
    font-weight: 400;
    font-size: 21px;
    line-height: 1.15;
    letter-spacing: 1px;
    padding: 0 20px;
  }
  .person {
    position: absolute;
    left: 0; right: 0;
    top: 267px;
    text-align: center;
  }
  .person__name {
    font-weight: 700;
    font-size: 30px;
    line-height: 1.1;
  }
  .person__role {
    font-size: 20px;
    line-height: 1.2;
  }
  .contact {
    position: absolute;
    left: 0; right: 0;
    top: 400px;
    text-align: center;
    list-style: none;
    font-size: 12.5px;
    line-height: 21.5px;
  }
  .contact__web { font-weight: 700; }
  .showcase { position: absolute; inset: 0; }
  .mini-name {
    font-family: "Caladea", Georgia, serif;
    font-size: 14px;
    fill: var(--white);
  }
</style>
</head>
<body>

<section class="card card--front" aria-label="Card front">
  <div class="brand-seal">
    <div class="brand-seal__disc">
      <span class="brand-name">Woven Glass and Tide</span>
    </div>
  </div>
  <div class="person">
    <h1 class="person__name">Helena Pikeworth</h1>
    <p class="person__role">Designer</p>
  </div>
  <ul class="contact">
    <li>Phone: 604.555.0172</li>
    <li class="contact__web">Website: www.WovenGlassandTide.example</li>
    <li>Email: Designer@WovenGlassandTide.example</li>
    <li>Blog: www.ShapingHillside.example</li>
  </ul>
</section>

<section class="card card--back" aria-label="Card back">
  <svg class="showcase" width="292" height="509" viewBox="0 0 292 509">
    <defs>
      <linearGradient id="tone-earrings" x1="0" y1="0" x2="1" y2="1">
        <stop offset="0" stop-color="#6b4a3a"/>
        <stop offset="0.5" stop-color="#e58a9a"/>
        <stop offset="1" stop-color="#c9d8cf"/>
      </linearGradient>
      <linearGradient id="tone-pot" x1="0" y1="0" x2="0" y2="1">
        <stop offset="0" stop-color="#c9b89c"/>
        <stop offset="0.5" stop-color="#7cc6cf"/>
        <stop offset="1" stop-color="#8a6a50"/>
      </linearGradient>
      <linearGradient id="tone-chimes" x1="0" y1="0" x2="1" y2="1">
        <stop offset="0" stop-color="#e9eef2"/>
        <stop offset="0.5" stop-color="#c07a56"/>
        <stop offset="1" stop-color="#d8dfe4"/>
      </linearGradient>
      <linearGradient id="tone-owl" x1="0" y1="0" x2="0" y2="1">
        <stop offset="0" stop-color="#8a6a4a"/>
        <stop offset="1" stop-color="#b9b3aa"/>
      </linearGradient>
    </defs>

    <g class="photo-rings" fill="var(--ring)">
      <circle cx="97" cy="104" r="84"/>
      <circle cx="199" cy="210" r="76"/>
      <circle cx="101" cy="327" r="82"/>
      <circle cx="185" cy="403" r="73"/>
      <circle cx="91" cy="447" r="40"/>
    </g>

    <circle cx="97" cy="104" r="73" fill="url(#tone-earrings)" role="img" aria-label="Photo of pink and mint stone drop earrings"/>
    <circle cx="199" cy="210" r="64" fill="url(#tone-pot)" role="img" aria-label="Photo of a turquoise glazed pottery vase"/>
    <circle cx="101" cy="327" r="70" fill="url(#tone-chimes)" role="img" aria-label="Photo of copper dangle earrings with beads"/>
    <circle cx="185" cy="403" r="61" fill="url(#tone-owl)" role="img" aria-label="Photo of a ceramic owl sculpture"/>

    <circle cx="91" cy="447" r="33" fill="var(--teal)"/>
    <text class="mini-name" x="91" y="452" text-anchor="middle">WGT</text>
  </svg>
</section>

</body>
</html>
```